Design a building access mobile app for Wopel by Quillstone Access Controls

Hello, We're looking for an awesome designer to create an app design for our app Wopel, by Quillstone Access Controls. the mobile app allows employees open their office doors with their mobile phone. this means they don't have to use those plastic card badges or keys. We like clean modern design, dark and light themes. We don't have a logo yet.

Target Market(s)

Commercial and employees

Industry/Entity Type

Building

Font styles to use
Sans Serif
Other font styles liked:
• Oswald extra light

Requirements
Must have
• nice clean design

```html
<!DOCTYPE html>
<html lang="en">
<head>
<meta charset="UTF-8">
<title>Wopel – Sign In</title>
<link rel="stylesheet" href="https://fonts.googleapis.com/css2?family=Nunito+Sans:wght@300;400&display=swap">
<style>
  :root {
    --backdrop: #fbf1d6;
    --screen: #ffffff;
    --hero-top: #9d9cc2;
    --hero-mid: #6c6a92;
    --hero-bottom: #23223a;
    --ink: #1d1d22;
    --muted: #9a9a9f;
    --rule: #ececec;
    --accent: #ff2e63;
    --on-accent: #ffe3ea;
  }
  * { margin: 0; padding: 0; box-sizing: border-box; }
  html, body {
    width: 1200px;
    height: 760px;
    overflow: hidden;
    background: var(--backdrop);
    font-family: "Nunito Sans", "Helvetica Neue", Arial, sans-serif;
  }
  .stage {
    width: 1200px;
    height: 760px;
    display: flex;
    align-items: center;
    justify-content: center;
  }
  .app-screen {
    position: relative;
    width: 380px;
    height: 700px;
    background: var(--screen);
    box-shadow: 0 24px 50px rgba(70, 60, 30, 0.25);
    display: flex;
    flex-direction: column;
  }
  .hero {
    position: relative;
    height: 290px;
    background:
      radial-gradient(ellipse 70% 30% at 50% 55%, rgba(200, 198, 220, 0.55), transparent 70%),
      linear-gradient(180deg, var(--hero-top) 0%, var(--hero-mid) 50%, var(--hero-bottom) 100%);
    display: flex;
    align-items: center;
    justify-content: center;
  }
  .hero-logo {
    color: #ffffff;
    font-weight: 300;
    font-size: 26px;
    letter-spacing: 5px;
  }
  .sign-in-form {
    flex: 1;
    display: flex;
    flex-direction: column;
    padding: 92px 44px 0;
  }
  .field {
    text-align: center;
    border-bottom: 1px solid var(--rule);
    padding-bottom: 14px;
    margin-bottom: 22px;
  }
  .field-label {
    display: block;
    font-size: 12px;
    font-weight: 300;
    color: var(--muted);
    margin-bottom: 4px;
  }
  .field-value {
    font-size: 18px;
    font-weight: 400;
    color: var(--ink);
  }
  .field-value.is-secret {
    letter-spacing: 5px;
    font-size: 20px;
    line-height: 24px;
  }
  .sign-in-button {
    margin: 28px -14px 0;
    height: 58px;
    background: var(--accent);
    color: var(--on-accent);
    border: none;
    font-family: inherit;
    font-weight: 300;
    font-size: 14px;
    letter-spacing: 2px;
  }
  .form-links {
    display: flex;
    justify-content: space-between;
    margin: 24px -14px 0;
    font-size: 12px;
    font-weight: 300;
    letter-spacing: 1.5px;
  }
  .link-forgot { color: var(--muted); }
  .link-signup { color: var(--accent); }
</style>
</head>
<body>
  <main class="stage">
    <section class="app-screen">
      <header class="hero" role="img" aria-label="Photograph of a misty pine forest in violet tones">
        <span class="hero-logo">LOGO</span>
      </header>
      <form class="sign-in-form">
        <div class="field">
          <span class="field-label">Username</span>
          <span class="field-value">ks99@example.com</span>
        </div>
        <div class="field">
          <span class="field-label">Password</span>
          <span class="field-value is-secret">••••••••</span>
        </div>
        <button class="sign-in-button" type="button">SIGN IN</button>
        <div class="form-links">
          <span class="link-forgot">FORGOT PASSWORD?</span>
          <span class="link-signup">SIGN UP</span>
        </div>
      </form>
    </section>
  </main>
</body>
</html>
```